Varrow Property Group Business cards

I am starting a property development and consultancy business called Varrow Property Group. I have a logo designed and a website on its way:
www.varrowgroup-example.com.au

I need a business card with the following:

Front:
Mostly orange with logo taking up all front of card

Back of card:
Logo

Miles Harcourt
Managing Director

T +61 455 207 364
E miles.harcourt@varrowgroup-example.com.au
www.varrowgroup-example.com.au

Industry/Entity Type

Business

Requirements
Must have
• curved edges

```html
<!DOCTYPE html>
<html lang="en">
<head>
<meta charset="utf-8">
<title>Varrow Property Group – Business Cards</title>
<link rel="stylesheet" href="https://fonts.googleapis.com/css2?family=Source+Sans+3:wght@400;600;700&display=swap">
<style>
  :root {
    --backdrop: #2a2a2a;
    --paper: #f3f3f1;
    --orange: #f0a91f;
    --orange-deep: #e6941a;
    --band-grey: #4b4b4b;
    --ink-dark: #3c3c3c;
    --ink-label: #5a4514;
    --rule: rgba(255, 255, 255, 0.55);
    --white: #ffffff;
  }
  * { box-sizing: border-box; margin: 0; padding: 0; }
  html, body {
    width: 1200px;
    height: 900px;
    overflow: hidden;
    background: var(--backdrop);
    font-family: "Source Sans 3", "Myriad Pro", sans-serif;
  }
  .canvas {
    position: relative;
    width: 1200px;
    height: 900px;
    display: flex;
    justify-content: center;
    align-items: center;
    gap: 60px;
  }
  .card {
    position: relative;
    width: 440px;
    height: 720px;
    border-radius: 22px;
    overflow: hidden;
    box-shadow: 0 18px 40px rgba(0, 0, 0, 0.45);
  }

  /* Details side */
  .card--details {
    background: linear-gradient(160deg, var(--orange) 0%, var(--orange-deep) 100%);
  }
  .details__logo-area {
    position: absolute;
    inset: 0 0 auto 0;
    height: 316px;
    background: var(--paper);
    display: flex;
    align-items: center;
    justify-content: center;
    border-bottom: 6px solid var(--white);
  }
  .wordmark {
    font-weight: 600;
    font-size: 34px;
    letter-spacing: 0.02em;
    text-align: center;
    line-height: 1.15;
  }
  .wordmark--dark { color: var(--ink-dark); }
  .details__name-band {
    position: absolute;
    left: 0;
    right: 0;
    top: 322px;
    height: 108px;
    background: var(--band-grey);
    border-bottom: 6px solid var(--white);
    padding: 22px 36px 0;
  }
  .person__name {
    color: var(--orange);
    font-weight: 700;
    font-size: 34px;
    line-height: 1.1;
  }
  .person__title {
    color: var(--white);
    font-size: 19px;
    margin-top: 4px;
  }
  .contact-list {
    position: absolute;
    left: 36px;
    right: 36px;
    top: 460px;
    list-style: none;
  }
  .contact-list__item {
    padding: 12px 0 14px;
    border-bottom: 1px solid var(--rule);
  }
  .contact-list__item:last-child { border-bottom: none; }
  .contact-list__label {
    display: block;
    color: var(--ink-label);
    font-weight: 600;
    font-size: 14px;
  }
  .contact-list__value {
    display: block;
    color: var(--white);
    font-size: 17px;
    margin-top: 2px;
    white-space: nowrap;
  }

  /* Logo side */
  .card--logo {
    background: linear-gradient(160deg, var(--orange) 0%, var(--orange-deep) 100%);
  }
  .logo-side__band {
    position: absolute;
    left: 0;
    right: 0;
    top: 110px;
    height: 150px;
    background: var(--paper);
    display: flex;
    align-items: center;
    justify-content: center;
  }
</style>
</head>
<body>
  <main class="canvas">
    <article class="card card--details" aria-label="Business card, details side">
      <header class="details__logo-area">
        <p class="wordmark wordmark--dark">Varrow<br>Property Group</p>
      </header>
      <section class="details__name-band">
        <h1 class="person__name">Miles Harcourt</h1>
        <p class="person__title">Managing Director</p>
      </section>
      <ul class="contact-list">
        <li class="contact-list__item">
          <span class="contact-list__label">Telephone:</span>
          <span class="contact-list__value">+61 455 207 364</span>
        </li>
        <li class="contact-list__item">
          <span class="contact-list__label">Email:</span>
          <span class="contact-list__value">miles.harcourt@varrowgroup-example.com.au</span>
        </li>
        <li class="contact-list__item">
          <span class="contact-list__label">Website:</span>
          <span class="contact-list__value">www.varrowgroup-example.com.au</span>
        </li>
      </ul>
    </article>

    <article class="card card--logo" aria-label="Business card, logo side">
      <div class="logo-side__band">
        <p class="wordmark wordmark--dark">Varrow<br>Property Group</p>
      </div>
    </article>
  </main>
</body>
</html>
```